Pinegate Health group for a medical office

We need a website created that for our new medical office that will support online booking for appointments. You designed the logo already.

```html
<!DOCTYPE html>
<html lang="en">
<head>
<meta charset="utf-8">
<title>Pinegate Health Group</title>
<link href="https://fonts.googleapis.com/css2?family=Montserrat:wght@500;600;700;800&family=Open+Sans:wght@400;600&display=swap" rel="stylesheet">
<style>
:root{
  --navy:#0c2a52;
  --navy-dark:#0a2142;
  --blue:#1b6fd1;
  --blue-bright:#2d8be6;
  --sky:#e9eff6;
  --grey-bg:#eef1f4;
  --text:#3b4656;
  --muted:#6b7685;
  --white:#ffffff;
}
*{box-sizing:border-box;margin:0;padding:0}
html,body{width:1200px;height:4360px;overflow:hidden}
body{font-family:"Open Sans",Arial,sans-serif;color:var(--text);background:var(--white);position:relative}
h1,h2,h3,h4,.brand,.btn,.nav a{font-family:"Montserrat",Arial,sans-serif}
section,header,footer{position:absolute;left:0;width:1200px}
.btn{display:inline-block;background:var(--blue);color:var(--white);font-size:15px;font-weight:600;padding:12px 26px;border-radius:4px;text-decoration:none}
.section-title{font-size:40px;font-weight:800;color:var(--navy);text-align:center;letter-spacing:.5px}
.divider{display:flex;align-items:center;justify-content:center;gap:10px;margin:14px 0 22px}
.divider span{width:60px;height:2px;background:var(--blue-bright)}
.divider i{width:14px;height:14px;border:2px solid var(--blue-bright);border-radius:50%}
.divider.left{justify-content:flex-start}
.photo{border-radius:6px}

/* header */
.site-header{top:0;height:128px;background:var(--white)}
.brand{position:absolute;left:112px;top:22px;display:flex;align-items:center;gap:12px}
.brand-mark{width:60px;height:60px;border-radius:50%;background:var(--blue)}
.brand-name{color:var(--navy);font-weight:800;font-size:30px;line-height:1}
.brand-name small{display:block;font-size:15px;letter-spacing:3px;margin-top:5px;font-weight:800}
.nav{position:absolute;left:530px;top:78px;display:flex;gap:48px}
.nav a{color:var(--navy);font-size:15px;font-weight:500;text-decoration:none}
.nav a.active{border-bottom:2px solid var(--blue);padding-bottom:6px}
.call{position:absolute;left:712px;top:18px;display:flex;gap:10px;align-items:center;font-size:14px;color:var(--navy)}
.call b{display:block;font-family:"Montserrat",sans-serif}
.header-btn{position:absolute;left:902px;top:14px;padding:12px 24px}

/* hero */
.hero{top:128px;height:600px;background:linear-gradient(90deg,#1d3a5c 0%,#3a5b80 40%,#9fb3c8 70%,#c9d5e1 100%)}
.hero-photo{position:absolute;right:0;top:0;width:700px;height:600px;background:linear-gradient(90deg,rgba(60,90,125,0) 0%,#a9bccf 40%,#d7e0ea 100%)}
.hero-content{position:absolute;left:112px;top:160px;width:720px;color:var(--white)}
.hero h1{font-size:48px;font-weight:800;line-height:1.18;white-space:nowrap}
.hero h1 em{font-style:normal;color:#4aa3ff}
.hero p{font-size:21px;margin:20px 0 34px;line-height:1.4;width:560px}

/* about */
.about{top:728px;height:732px}
.about-photo{position:absolute;left:112px;top:232px;width:448px;height:440px;background:linear-gradient(160deg,#c8d4df,#8ea3b8)}
.about-badge{position:absolute;left:384px;top:456px;width:216px;height:216px;background:var(--blue);color:var(--white);padding:40px 24px}
.about-badge strong{font-family:"Montserrat",sans-serif;font-size:48px;font-weight:800;display:block}
.about-badge span{font-size:19px;line-height:1.3}
.about-body{position:absolute;left:640px;top:116px;width:450px}
.about-body h2{font-size:40px;font-weight:800;color:var(--navy)}
.about-body p{font-size:15.5px;line-height:1.65}
.about-body .btn{margin-top:28px}
.about-values{position:absolute;left:600px;top:442px;width:490px;height:230px;background:var(--sky);display:flex;padding:28px 0 0 30px;gap:30px}
.value{width:200px}
.value-icon{width:44px;height:44px}
.value h4{color:var(--navy);font-size:18px;margin:10px 0 8px}
.value p{font-size:13px;color:var(--muted);line-height:1.45}

/* services */
.services{top:1460px;height:732px;background:var(--grey-bg)}
.services .section-title{margin-top:100px}
.services .intro{width:720px;margin:0 auto;text-align:center;font-size:16px;line-height:1.6}
.service-cards{position:absolute;left:112px;top:288px;display:flex;gap:44px}
.service-card{width:296px;height:352px;background:var(--white);border-radius:6px;overflow:hidden;text-align:center;position:relative}
.service-card .photo{height:196px;border-radius:0}
.service-card .icon{position:absolute;left:116px;top:160px;width:64px;height:64px;border-radius:50%;background:var(--blue);border:4px solid var(--white)}
.service-card h3{margin-top:46px;color:var(--navy);font-size:22px;font-weight:700}
.service-card p{font-size:14px;color:var(--muted);padding:10px 40px 0;line-height:1.5}
.arrow{position:absolute;top:450px;width:36px;height:36px;border-radius:50%;background:var(--navy)}
.arrow svg{display:block}

/* why */
.why{top:2192px;height:588px}
.why h2{position:absolute;left:112px;top:140px;font-size:40px;font-weight:800;color:var(--navy)}
.why .divider{position:absolute;left:112px;top:190px}
.why .intro{position:absolute;left:640px;top:140px;width:450px;font-size:15.5px;line-height:1.6}
.why-cards{position:absolute;left:112px;top:256px;display:flex;gap:16px}
.why-card{width:232px;height:212px;background:var(--white);box-shadow:0 4px 18px rgba(12,42,82,.12);border-radius:6px;text-align:center;padding-top:26px}
.why-card svg{width:64px;height:64px}
.why-card h4{color:var(--navy);font-size:18px;margin:8px 0 10px;white-space:nowrap}
.why-card p{font-size:13.5px;color:var(--muted);padding:0 26px;line-height:1.45}

/* cta */
.cta{top:2780px;height:452px;background:linear-gradient(110deg,#0e3f86 0%,#1b6fd1 55%,#4aa3ff 100%);text-align:center;color:var(--white)}
.cta h2{font-size:42px;font-weight:800;margin-top:104px}
.cta .divider span{background:var(--white)}
.cta .divider i{border-color:var(--white)}
.cta p{width:620px;margin:0 auto 32px;font-size:16px;line-height:1.65}
.cta .btn{background:var(--navy-dark)}

/* team */
.team{top:3232px;height:696px}
.team .section-title{margin-top:112px}
.team .intro{width:640px;margin:0 auto;text-align:center;font-size:16px;line-height:1.6}
.team-cards{position:absolute;left:112px;top:286px;display:flex;gap:16px}
.member{width:232px;height:316px;position:relative;border-radius:6px;overflow:hidden;background:var(--sky)}
.member .photo{height:316px;border-radius:0}
.member-info{position:absolute;left:0;bottom:0;width:100%;height:98px;background:var(--sky);color:var(--navy);padding:20px 20px}
.member:first-child .member-info{background:rgba(27,111,209,.92);color:var(--white)}
.member-info h4{font-size:20px}
.member-info p{font-size:14px;margin-top:4px}

/* footer */
.site-footer{top:3928px;height:432px;background:var(--navy-dark);color:#d3dcea}
.footer-col{position:absolute;top:64px}
.footer-col h4{color:var(--white);font-size:19px;margin-bottom:20px}
.footer-col p,.footer-col li{font-size:14.5px;line-height:1.9;list-style:none}
.newsletter input{display:block;width:290px;height:44px;border:0;border-radius:4px;margin:22px 0 14px;padding:0 14px;font-size:14px}
.newsletter-row{display:flex;align-items:center;gap:16px}
.newsletter .btn{padding:10px 26px;font-size:14px}
.social{width:24px;height:24px;border-radius:50%;background:#d3dcea}
.contact-line{display:flex;gap:12px;align-items:flex-start;margin-bottom:14px}
.copyright{position:absolute;left:0;bottom:0;width:100%;height:40px;background:#081a35;text-align:center;font-size:13px;line-height:40px;color:#b9c4d4}
.chat{position:absolute;left:1124px;top:4274px;width:52px;height:52px;border-radius:50%;background:var(--blue-bright)}
</style>
</head>
<body>

<header class="site-header">
  <div class="brand">
    <div class="brand-mark"></div>
    <div class="brand-name">PINEGATE<small>HEALTH GROUP</small></div>
  </div>
  <div class="call">
    <svg width="26" height="26" viewBox="0 0 24 24"><path fill="#1b6fd1" d="M6.6 10.8a15 15 0 006.6 6.6l2.2-2.2c.3-.3.7-.4 1-.2 1.1.4 2.3.6 3.6.6.6 0 1 .4 1 1V20c0 .6-.4 1-1 1C10.6 21 3 13.4 3 4c0-.6.4-1 1-1h3.5c.6 0 1 .4 1 1 0 1.3.2 2.5.6 3.6.1.3 0 .7-.2 1z"/></svg>
    <div><b>Call Us :</b>+1 800 555 0142</div>
  </div>
  <a class="btn header-btn" href="#">Book an Appointment</a>
  <nav class="nav">
    <a class="active" href="#">Home</a><a href="#">Services</a><a href="#">New Patients</a><a href="#">About Us</a><a href="#">Contact Us</a>
  </nav>
</header>

<section class="hero">
  <div class="hero-photo" role="img" aria-label="Photo of a smiling doctor in a white coat writing on a clipboard in a bright clinic"></div>
  <div class="hero-content">
    <h1>HEALTHCARE THAT<br>RUNS LIKE <em>PINEGATE</em></h1>
    <p>A streamlined medical practice offering expert care with easy online appointment scheduling.</p>
    <a class="btn" href="#">Book an Appointment</a>
  </div>
</section>

<section class="about">
  <div class="about-photo photo" role="img" aria-label="Photo of a doctor with a stethoscope, arms crossed, in a clinic hallway"></div>
  <div class="about-badge"><strong>100%</strong><span>Patient-Focused Care</span></div>
  <div class="about-body">
    <h2>ABOUT US</h2>
    <div class="divider left"><span></span><i></i><span></span></div>
    <p>At Pinegate Health Group, our focus is simple: providing dependable medical care in a welcoming and efficient environment. We are committed to making every visit easy, comfortable, and on time, so you can focus on what matters most—your health.</p>
    <a class="btn" href="#">Read More</a>
  </div>
  <div class="about-values">
    <div class="value">
      <svg class="value-icon" viewBox="0 0 44 44"><circle cx="22" cy="22" r="20" fill="none" stroke="#1b6fd1" stroke-width="2"/><circle cx="22" cy="22" r="11" fill="none" stroke="#1b6fd1" stroke-width="2"/><circle cx="22" cy="22" r="3" fill="#1b6fd1"/></svg>
      <h4>Our Mission</h4>
      <p>Risus commodo viverra maecenas accumsan lacus vel facilisis.</p>
    </div>
    <div class="value">
      <svg class="value-icon" viewBox="0 0 44 44"><path d="M3 22c5-9 12-13 19-13s14 4 19 13c-5 9-12 13-19 13S8 31 3 22z" fill="none" stroke="#1b6fd1" stroke-width="2"/><circle cx="22" cy="22" r="6" fill="#1b6fd1"/></svg>
      <h4>Our Vision</h4>
      <p>Risus commodo viverra maecenas accumsan lacus vel facilisis.</p>
    </div>
  </div>
</section>

<section class="services">
  <h2 class="section-title">OUR SERVICES</h2>
  <div class="divider"><span></span><i></i><span></span></div>
  <p class="intro">We offer personalized, high-quality medical care with convenient scheduling, clear communication, and a commitment to making every visit smooth and stress-free.</p>
  <div class="arrow" style="left:56px"><svg width="36" height="36" viewBox="0 0 36 36"><path d="M21 11l-7 7 7 7" fill="none" stroke="#fff" stroke-width="3"/></svg></div>
  <div class="arrow" style="left:1108px"><svg width="36" height="36" viewBox="0 0 36 36"><path d="M15 11l7 7-7 7" fill="none" stroke="#fff" stroke-width="3"/></svg></div>
  <div class="service-cards">
    <article class="service-card">
      <div class="photo" role="img" aria-label="Photo of a doctor consulting with a patient" style="background:linear-gradient(150deg,#d9c7b5,#9aaebf)"></div>
      <div class="icon"></div>
      <h3>Primary Care</h3>
      <p>Risus commodo viverra mae cenas accumsan lacus vel facilisis.</p>
    </article>
    <article class="service-card">
      <div class="photo" role="img" aria-label="Photo of a doctor checking an older patient with a stethoscope" style="background:linear-gradient(150deg,#c7d3de,#8aa0b6)"></div>
      <div class="icon"></div>
      <h3>Preventive Care</h3>
      <p>Risus commodo viverra mae cenas accumsan lacus vel facilisis.</p>
    </article>
    <article class="service-card">
      <div class="photo" role="img" aria-label="Photo of a doctor greeting a mother and child" style="background:linear-gradient(150deg,#e0cdbb,#a8b7c6)"></div>
      <div class="icon"></div>
      <h3>Same-Day Visits</h3>
      <p>Risus commodo viverra mae cenas accumsan lacus vel facilisis.</p>
    </article>
  </div>
</section>

<section class="why">
  <h2>WHY CHOOSE US</h2>
  <div class="divider left"><span></span><i></i><span></span></div>
  <p class="intro">Lorem ipsum dolor sit amet, consectetur adipiscing elit, sed do eiusmod tempor incididunt ut labore et dolore magna aliqua.</p>
  <div class="why-cards">
    <div class="why-card">
      <svg viewBox="0 0 64 64"><circle cx="32" cy="22" r="10" fill="none" stroke="#1b6fd1" stroke-width="2.5"/><path d="M14 54c2-12 9-18 18-18s16 6 18 18" fill="none" stroke="#1b6fd1" stroke-width="2.5"/></svg>
      <h4>Patient-First Care</h4>
      <p>Risus commodo viverra mae cenas accumsan lacus vel facilisis.</p>
    </div>
    <div class="why-card">
      <svg viewBox="0 0 64 64"><rect x="18" y="6" width="28" height="52" rx="4" fill="none" stroke="#1b6fd1" stroke-width="2.5"/><rect x="24" y="20" width="16" height="14" fill="none" stroke="#1b6fd1" stroke-width="2"/><path d="M27 27l3 3 6-6" fill="none" stroke="#1b6fd1" stroke-width="2"/></svg>
      <h4>Easy Online Booking</h4>
      <p>Risus commodo viverra mae cenas accumsan lacus vel facilisis.</p>
    </div>
    <div class="why-card">
      <svg viewBox="0 0 64 64"><circle cx="32" cy="34" r="22" fill="none" stroke="#1b6fd1" stroke-width="2.5"/><path d="M32 20v14l9 6" fill="none" stroke="#1b6fd1" stroke-width="2.5"/></svg>
      <h4>On-Time Visits</h4>
      <p>Risus commodo viverra mae cenas accumsan lacus vel facilisis.</p>
    </div>
    <div class="why-card">
      <svg viewBox="0 0 64 64"><path d="M18 10v16a10 10 0 0020 0V10" fill="none" stroke="#1b6fd1" stroke-width="2.5"/><path d="M28 36v6a10 10 0 0020 0v-8" fill="none" stroke="#1b6fd1" stroke-width="2.5"/><circle cx="48" cy="30" r="4" fill="none" stroke="#1b6fd1" stroke-width="2.5"/></svg>
      <h4>Experienced Providers</h4>
      <p>Risus commodo viverra mae cenas accumsan lacus vel facilisis.</p>
    </div>
  </div>
</section>

<section class="cta">
  <h2>READY TO BOOK YOUR VISIT?</h2>
  <div class="divider"><span></span><i></i><span></span></div>
  <p>At Pinegate Health Group, our focus is simple: providing dependable medical care in a welcoming and efficient environment. We are committed to making every visit easy, comfortable, and on time, so you can focus on what matters most—your health.</p>
  <a class="btn" href="#">Book an Appointment</a>
</section>

<section class="team">
  <h2 class="section-title">OUR TEAM</h2>
  <div class="divider"><span></span><i></i><span></span></div>
  <p class="intro">Our team is made up of experienced medical professionals dedicated to providing reliable, patient-centered care in a modern and welcoming environment.</p>
  <div class="team-cards">
    <div class="member"><div class="photo" role="img" aria-label="Portrait photo of a team physician" style="background:linear-gradient(160deg,#cdd8e3,#8fa4b9)"></div><div class="member-info"><h4>Lorem Ipsum</h4><p>Risus commodo viverra mae</p></div></div>
    <div class="member"><div class="photo" role="img" aria-label="Portrait photo of a team physician" style="background:linear-gradient(160deg,#dfe6ee,#a9b9c9)"></div><div class="member-info"><h4>Lorem Ipsum</h4><p>Risus commodo viverra mae</p></div></div>
    <div class="member"><div class="photo" role="img" aria-label="Portrait photo of a team physician" style="background:linear-gradient(160deg,#d8c8b8,#90a3b6)"></div><div class="member-info"><h4>Lorem Ipsum</h4><p>Risus commodo viverra mae</p></div></div>
    <div class="member"><div class="photo" role="img" aria-label="Portrait photo of a team physician" style="background:linear-gradient(160deg,#e2d3c4,#b3c1cf)"></div><div class="member-info"><h4>Lorem Ipsum</h4><p>Risus commodo viverra mae</p></div></div>
  </div>
</section>

<footer class="site-footer">
  <div class="footer-col newsletter" style="left:112px;width:300px">
    <h4>Join the Care You Can Trust</h4>
    <p>Experience patient-focused care with easy scheduling and trusted providers.</p>
    <input type="email" placeholder="Email" aria-label="Email">
    <div class="newsletter-row">
      <a class="btn" href="#">Submit</a>
      <span class="social" aria-label="Social link"></span>
      <span class="social" aria-label="Social link"></span>
      <span class="social" aria-label="Social link"></span>
    </div>
  </div>
  <div class="footer-col" style="left:484px">
    <h4>Main Links</h4>
    <ul><li>Home</li><li>About Us</li><li>Appointments</li><li>Services</li><li>Contact Us</li></ul>
  </div>
  <div class="footer-col" style="left:664px;width:230px">
    <h4>Contact Us</h4>
    <div class="contact-line"><svg width="18" height="22" viewBox="0 0 18 22"><path d="M9 1a7 7 0 017 7c0 5-7 13-7 13S2 13 2 8a7 7 0 017-7z" fill="#2d8be6"/><circle cx="9" cy="8" r="2.5" fill="#0a2142"/></svg><p style="line-height:1.5">45 Pinegate Avenue,<br>Suite 210</p></div>
    <div class="contact-line"><svg width="18" height="18" viewBox="0 0 24 24"><path fill="#2d8be6" d="M6.6 10.8a15 15 0 006.6 6.6l2.2-2.2c.3-.3.7-.4 1-.2 1.1.4 2.3.6 3.6.6.6 0 1 .4 1 1V20c0 .6-.4 1-1 1C10.6 21 3 13.4 3 4c0-.6.4-1 1-1h3.5c.6 0 1 .4 1 1 0 1.3.2 2.5.6 3.6.1.3 0 .7-.2 1z"/></svg><p style="line-height:1.3">+1 800 555 0142</p></div>
    <div class="contact-line"><svg width="18" height="18" viewBox="0 0 24 24"><rect x="2" y="5" width="20" height="14" rx="2" fill="#2d8be6"/><path d="M3 6l9 7 9-7" fill="none" stroke="#0a2142" stroke-width="2"/></svg><p style="line-height:1.3">info@pinegatehealth.example</p></div>
  </div>
  <div class="footer-col" style="left:980px">
    <h4>Other Links</h4>
    <ul><li>Privacy Policy</li><li>HIPAA Notice</li><li>Cookies Policy</li><li>Patient Portal</li><li>Insurance Info</li></ul>
  </div>
  <div class="copyright">Copyright © 2026 Pinegate Health Group. All rights reserved.</div>
</footer>
<div class="chat" aria-label="Chat"><svg width="52" height="52" viewBox="0 0 52 52"><path d="M15 17h22a3 3 0 013 3v11a3 3 0 01-3 3H24l-6 5v-5h-3a3 3 0 01-3-3V20a3 3 0 013-3z" fill="#fff"/></svg></div>
</body>
</html>
```